/ custom plush toys for luxury hotel /

We are, a US company that makes custom plush toys for luxury hotels only. (our customers)
our logo is a mascot:
a teddy bear dressing up as a hotel concierge, the message is: in terms of teddy bear we are your concierge
These plushies are intended to be offered to the children of the customers of these luxurious hotels.
To convince our customers who will land on this site to contact us and work with us, we want to convey the message that our client (the hotel) will make HIS client and HIS children happy by offering them an unexpected gift at the check-in , also to make understand that it is very powerful advertising and marketing object for the hotel (this plush and its LOGO obviously will accompany the children of these customers everywhere).
We also want to insist on the fact that our solution is turnkey, starting from your wishes we take care of everything from the creation of the design to the delivery of the finished products, you do not worry about anything else.
Here is our process:
We only do custom, the customer gives us his theme and ideas and from that we propose different designs, drawing, 3D visualizations, once the design is approved, we make a physical sample that we have validated or modified by our client...
We would like to have a website/landing page to present our concept and our company, also to involve our future customers to contact us by mail or phone, this should be the objective of this page
We want to use themes like teddy bear, luxury, , kids, custom made, handmade, hand drawing..
We really want to emphasize the customization: we create your teddy bear from scratch.
We do not have a catalog because made-to-measure and therefore really want to involve our future customers to contact us by mail.
I can provide you with some of this content (sources file available):
Our Logo
Pictures of some plushies that we made this year
Drawings,
3D
a brief comic strip that we made to present us
Here are some examples attached .
also: Some content that I don't have but that I think would fit in the thematic:
happy children with a teddy bear /
the steps of manufacturing (a seamstress? / the selection of a fabric?) / a designer at work on a drawing board /
etc
Waiting for your proposal,
available if precisions needed
Thank you for your time
Tobi
Luxury Hotel Manager / Purchaser

```html
<!DOCTYPE html>
<html lang="en">
<head>
<meta charset="utf-8">
<title>PlushKeep — Custom plush toys for luxury hotels</title>
<link href="https://fonts.googleapis.com/css2?family=Montserrat:wght@400;500;600;700;800&family=Caveat:wght@500&display=swap" rel="stylesheet">
<style>
:root{
  --navy:#25305f;
  --navy-deep:#15123d;
  --brown:#6b3a1f;
  --brown-red:#a8431c;
  --yellow:#fdd57f;
  --gold:#f6c453;
  --peach:#fdd6c5;
  --orange:#f39a3f;
  --ink:#1d1d2b;
  --text:#4a4a55;
  --field:#ececec;
  --white:#fff;
}
*{box-sizing:border-box;margin:0;padding:0}
html,body{width:1200px;height:5059px;overflow:hidden}
body{font-family:"Montserrat",sans-serif;color:var(--ink);background:var(--white);position:relative}
.abs{position:absolute}
a{text-decoration:none;color:inherit}
.btn{position:absolute;display:flex;align-items:center;justify-content:center;gap:12px;border-radius:30px;font-weight:700;font-size:15px}
.btn-outline{background:var(--navy);color:#fff;border:3px solid var(--navy);box-shadow:inset 0 0 0 2px #fff}
.btn-orange{border:2px solid var(--orange)}
.arrow{width:26px;height:10px}
.photo{position:absolute;overflow:hidden}
/* header */
.site-header{position:absolute;left:0;top:0;width:1200px;height:95px;background:#fff;z-index:3}
.logo-badge{position:absolute;left:110px;top:0;width:104px;height:135px;border-radius:0 0 52px 52px;background:#fff;display:flex;align-items:flex-end;justify-content:center;padding-bottom:18px}
.logo-badge span{font-weight:700;font-size:15px;color:var(--brown)}
.nav a{position:absolute;top:36px;font-size:15px;font-weight:500;color:var(--ink)}
.call-btn{position:absolute;left:923px;top:24px;width:183px;height:47px;border-radius:24px;background:var(--brown-red);color:#fff;font-weight:700;font-size:16px;display:flex;align-items:center;justify-content:center;gap:10px}
/* hero */
.hero{position:absolute;left:0;top:95px;width:1200px;height:528px;background:linear-gradient(90deg,#2c3a6c,#34437a 60%,#2b3a6a);overflow:hidden}
.hero-floor{position:absolute;left:0;bottom:0;width:1200px;height:55px;background:linear-gradient(#d9d6d1,#b9b2aa)}
.hero .script{position:absolute;left:92px;top:130px;font-family:"Caveat",cursive;font-size:44px;color:#fff}
.hero h1{position:absolute;left:92px;top:170px;font-size:78px;font-weight:800;color:var(--gold);line-height:1}
.hero .sub{position:absolute;left:92px;top:255px;font-size:50px;font-weight:500;color:#fff}
.hero-circle{position:absolute;left:672px;top:18px;width:524px;height:524px;border-radius:50%;background:linear-gradient(135deg,var(--gold),var(--orange));}
/* about */
.about-blob{position:absolute;left:98px;top:707px;width:432px;height:462px;border-radius:48% 52% 55% 45%/45% 50% 50% 55%;background:radial-gradient(circle at 45% 55%,#f4d7c9,#ececec 70%)}
.section-title{font-size:32px;font-weight:700;color:var(--ink)}
.eyebrow{font-size:16px;font-weight:500;color:var(--brown-red)}
.body-copy{font-size:15px;line-height:31px;color:var(--text)}
/* process */
.process{position:absolute;left:0;top:1251px;width:1200px;height:746px;background:var(--yellow)}
.center{text-align:center;width:1200px;left:0}
.step-card{position:absolute;top:251px;width:232px;height:325px;border-radius:116px 116px 116px 116px}
.step-tag{position:absolute;top:206px;width:76px;height:56px;background:var(--brown);color:#fff;font-weight:800;font-size:24px;display:flex;align-items:center;justify-content:center;clip-path:polygon(30% 0,70% 0,100% 100%,0 100%);padding-top:8px}
.step-text{position:absolute;top:595px;width:220px;padding-left:14px;border-left:3px solid var(--brown);font-size:15px;font-weight:500;line-height:26px;color:var(--ink)}
/* gallery */
.tile{position:absolute;border-radius:22px}
/* steps */
.steps{position:absolute;left:0;top:3439px;width:1200px;height:542px;background:var(--peach)}
.steps-pill{position:absolute;left:365px;top:3408px;width:470px;height:62px;border-radius:31px;background:var(--brown);color:#fff;font-size:31px;font-weight:700;display:flex;align-items:center;justify-content:center;z-index:2}
.mstep{position:absolute;width:260px;text-align:center;font-size:16px;line-height:31px;color:var(--text)}
.mstep b{display:block;font-size:17px;color:var(--ink);font-weight:700}
/* contact */
.field{position:absolute;background:var(--field);border-radius:4px;font-size:15px;color:#555;padding:16px 18px}
/* footer */
.site-footer{position:absolute;left:0;top:4635px;width:1200px;height:424px;background:var(--navy-deep);color:#fff}
.foot-h{position:absolute;top:96px;font-size:18px;font-weight:700}
.foot-l{position:absolute;font-size:16px;color:#e7e6f2}
</style>
</head>
<body>

<header class="site-header">
  <div class="logo-badge"><span>PlushKeep</span></div>
  <nav class="nav">
    <a style="left:367px">Home</a>
    <a style="left:457px">About Us</a>
    <a style="left:576px">Products</a>
    <a style="left:691px">Gallery</a>
    <a style="left:792px">Contact Us</a>
  </nav>
  <a class="call-btn"><svg width="16" height="16" viewBox="0 0 24 24" fill="#fff"><path d="M6.6 10.8a15 15 0 0 0 6.6 6.6l2.2-2.2c.3-.3.7-.4 1-.2 1.1.4 2.3.6 3.6.6.6 0 1 .4 1 1V20c0 .6-.4 1-1 1A17 17 0 0 1 3 4c0-.6.4-1 1-1h3.5c.6 0 1 .4 1 1 0 1.3.2 2.5.6 3.6.1.3 0 .7-.2 1z"/></svg>555-014-2290</a>
</header>

<section class="hero">
  <div class="hero-floor"></div>
  <p class="script">We create your</p>
  <h1>teddy bear</h1>
  <p class="sub">from scratch.</p>
  <a class="btn btn-outline btn-orange" style="left:96px;top:345px;width:181px;height:45px;border-color:var(--orange);box-shadow:none">Contact Us <svg class="arrow" viewBox="0 0 26 10"><path d="M0 5h23M19 1l4 4-4 4" stroke="#fff" stroke-width="2" fill="none"/></svg></a>
  <div class="hero-circle"></div>
  <div class="photo" role="img" aria-label="Happy child hugging a teddy bear" style="left:684px;top:30px;width:500px;height:500px;border-radius:50%;background:linear-gradient(135deg,#f7b25b,#e58a3b 55%,#c9a27e)"></div>
  <svg class="abs" style="left:1030px;top:40px" width="56" height="56" viewBox="0 0 56 56"><g stroke="#fff" stroke-width="8" stroke-linecap="round"><path d="M6 12 18 2"/><path d="M16 30 34 14"/><path d="M34 44 52 28"/></g></svg>
  <svg class="abs" style="left:650px;top:320px" width="56" height="56" viewBox="0 0 56 56"><g stroke="#fff" stroke-width="8" stroke-linecap="round"><path d="M6 20 22 6"/><path d="M6 40 34 16"/><path d="M22 50 40 34"/></g></svg>
</section>

<section aria-label="About">
  <div class="about-blob" role="img" aria-label="Custom plush dog with a pink bag"></div>
  <svg class="abs" style="left:198px;top:716px" width="82" height="82" viewBox="0 0 82 82"><defs><clipPath id="c1"><circle cx="41" cy="41" r="40"/></clipPath></defs><g clip-path="url(#c1)" stroke="var(--navy)" stroke-width="4">
  <path d="M-20 60 60-20M-10 70 70-10M0 80 80 0M10 90 90 10M20 100 100 20M-30 50 50-30M30 110 110 30"/></g></svg>
  <svg class="abs" style="left:378px;top:1098px" width="60" height="32" viewBox="0 0 60 32"><g stroke="var(--gold)" stroke-width="3"><path d="M2 30 28 4M12 30 38 4M22 30 48 4M32 30 58 4"/></g></svg>
  <h2 class="abs section-title" style="left:599px;top:769px">About PlushKeep</h2>
  <p class="abs eyebrow" style="left:599px;top:825px;width:520px;line-height:26px">We are PlushKeep, a US company that makes custom plush toys for luxury hotels only.</p>
  <p class="abs body-copy" style="left:599px;top:892px;width:520px">Lorem ipsum dolor sit amet consectetur adipisicing elitso sed do eiusmod tempor incididunt ut labore et dolore sid magna aliqua. Ut enim ad minim veniam, quis nostrud exe citation ullamco laboris nisi ut aliquipcommodo conse.</p>
  <a class="btn btn-outline btn-orange" style="left:599px;top:1045px;width:177px;height:49px;border-color:var(--brown-red);box-shadow:none">View More <svg class="arrow" viewBox="0 0 26 10"><path d="M0 5h23M19 1l4 4-4 4" stroke="#fff" stroke-width="2" fill="none"/></svg></a>
  <div class="abs" style="left:809px;top:1046px;width:47px;height:47px;border-radius:8px;background:var(--brown-red);display:flex;align-items:center;justify-content:center"><svg width="18" height="18" viewBox="0 0 24 24" fill="#fff"><path d="M6.6 10.8a15 15 0 0 0 6.6 6.6l2.2-2.2c.3-.3.7-.4 1-.2 1.1.4 2.3.6 3.6.6.6 0 1 .4 1 1V20c0 .6-.4 1-1 1A17 17 0 0 1 3 4c0-.6.4-1 1-1h3.5c.6 0 1 .4 1 1 0 1.3.2 2.5.6 3.6.1.3 0 .7-.2 1z"/></svg></div>
  <p class="abs" style="left:874px;top:1048px;font-size:14px;font-weight:600;color:var(--brown-red);line-height:22px">Call Us:<br><b>555-014-2290</b></p>
</section>

<section class="process">
  <h2 class="abs center section-title" style="top:74px">Here is Our Process</h2>
  <p class="abs center eyebrow" style="top:124px;font-size:16px">We only do custom</p>
  <div class="step-tag" style="left:172px">01</div>
  <div class="step-tag" style="left:432px">02</div>
  <div class="step-tag" style="left:692px">03</div>
  <div class="step-tag" style="left:952px">04</div>
  <svg class="abs" style="left:296px;top:212px" width="90" height="50" viewBox="0 0 90 50"><path d="M4 44C30 46 60 30 78 6" stroke="var(--ink)" stroke-width="1.5" stroke-dasharray="4 4" fill="none"/><path d="M72 6h8v8" stroke="var(--ink)" stroke-width="1.5" fill="none"/></svg>
  <svg class="abs" style="left:558px;top:212px" width="90" height="50" viewBox="0 0 90 50"><path d="M4 10C30 -2 64 8 80 40" stroke="var(--ink)" stroke-width="1.5" stroke-dasharray="4 4" fill="none"/><path d="M74 40h7v-8" stroke="var(--ink)" stroke-width="1.5" fill="none"/></svg>
  <svg class="abs" style="left:818px;top:212px" width="90" height="50" viewBox="0 0 90 50"><path d="M4 44C30 46 60 30 78 6" stroke="var(--ink)" stroke-width="1.5" stroke-dasharray="4 4" fill="none"/><path d="M72 6h8v8" stroke="var(--ink)" stroke-width="1.5" fill="none"/></svg>
  <div class="step-card photo" role="img" aria-label="Customer's theme: a colourful reef fish" style="left:92px;background:linear-gradient(160deg,#8fa3a8,#5a7f70 60%,#c9b68e)"></div>
  <div class="step-card photo" role="img" aria-label="Designer drawing plush concepts" style="left:354px;background:linear-gradient(160deg,#3c3a3a,#7a5d4c 55%,#c8412c)"></div>
  <div class="step-card photo" role="img" aria-label="3D visualization of the fish plush" style="left:613px;background:linear-gradient(160deg,#e8e8e8,#c9d3d6 55%,#5f8ea0)"></div>
  <div class="step-card photo" role="img" aria-label="Physical sample of the fish plush" style="left:874px;background:linear-gradient(160deg,#eef0f2,#a8d6dc 55%,#e89a5a)"></div>
  <p class="step-text" style="left:92px">The customer gives us his theme and ideas and from that</p>
  <p class="step-text" style="left:354px">We propose different designs, drawing, 3D visualizations</p>
  <p class="step-text" style="left:613px">Once the design is approved, you we started working</p>
  <p class="step-text" style="left:874px">we make a physical sample that we have validated</p>
</section>

<section aria-label="Luxury hotels">
  <h2 class="abs section-title" style="left:92px;top:2095px;line-height:43px">We Do This<br>Only For Luxury Hotel</h2>
  <p class="abs body-copy" style="left:92px;top:2198px;width:510px">Eaque ipsa quae ab illo inventore veritatis et quasi archite to beatae vitae dicta sunt explicabo. Nemo enim ipsamvo ptatem quia voluptas sit aspernatur aut odit aut fugit, sed quia consequuntur magni dolores eos qui ratione volupist tatem sequi nesciunt. Neque porro quisquam est dolorem ipsum quia dolor sit amet consectetur, adipisci velit.</p>
  <a class="btn btn-outline" style="left:92px;top:2414px;width:187px;height:47px">Contact Us <svg class="arrow" viewBox="0 0 26 10"><path d="M0 5h23M19 1l4 4-4 4" stroke="#fff" stroke-width="2" fill="none"/></svg></a>
  <div class="abs" style="left:696px;top:2080px;width:410px;height:410px;border-radius:50%;border:3px solid var(--orange)"></div>
  <div class="photo" role="img" aria-label="Luxury hotel with pool and gardens" style="left:712px;top:2096px;width:378px;height:378px;border-radius:50%;background:linear-gradient(180deg,#9cc3e4,#d9dde2 45%,#6f8d7a 70%,#d6cbbb)"></div>
  <svg class="abs" style="left:1028px;top:2072px" width="56" height="56" viewBox="0 0 56 56"><g stroke-width="8" stroke-linecap="round"><path d="M6 20 18 8" stroke="var(--gold)"/><path d="M22 22 40 6" stroke="var(--navy)"/><path d="M28 42 46 26" stroke="var(--gold)"/></g></svg>
  <svg class="abs" style="left:700px;top:2418px" width="56" height="56" viewBox="0 0 56 56"><g stroke-width="8" stroke-linecap="round"><path d="M8 22 24 8" stroke="var(--navy)"/><path d="M6 42 24 26" stroke="var(--gold)"/><path d="M30 44 46 30" stroke="var(--gold)"/></g></svg>
</section>

<section aria-label="Gallery">
  <h2 class="abs center section-title" style="top:2648px">Some Plushies</h2>
  <p class="abs center eyebrow" style="top:2702px">that we made this year</p>
  <div class="tile photo" role="img" aria-label="Grey plush bulldog with red bandana" style="left:92px;top:2779px;width:246px;height:324px;background:linear-gradient(160deg,#f2f2f2,#6c6d72 60%,#d6403c)"></div>
  <div class="tile photo" role="img" aria-label="Plush dog" style="left:92px;top:3113px;width:246px;height:216px;background:linear-gradient(160deg,#f4f4f4,#e7c9a4)"></div>
  <div class="tile" style="left:350px;top:2779px;width:243px;height:216px;background:var(--yellow);display:flex;align-items:center;justify-content:center" role="img" aria-label="Pink plush bag, enlarge view"><div style="width:44px;height:44px;border-radius:50%;background:#fff;display:flex;align-items:center;justify-content:center"><svg width="20" height="20" viewBox="0 0 20 20"><circle cx="8" cy="8" r="6" stroke="var(--ink)" stroke-width="2" fill="none"/><path d="M12.5 12.5 18 18M8 5v6M5 8h6" stroke="var(--ink)" stroke-width="2"/></svg></div></div>
  <div class="tile photo" role="img" aria-label="White plush turtle" style="left:350px;top:3005px;width:243px;height:324px;background:linear-gradient(160deg,#dedede,#f4f4f4 50%,#9c9c9c)"></div>
  <div class="tile photo" role="img" aria-label="Beige plush bulldog" style="left:605px;top:2779px;width:245px;height:324px;background:linear-gradient(160deg,#c7bfb6,#d9c39a 55%,#d75c7a)"></div>
  <div class="tile photo" role="img" aria-label="Colourful plush fish" style="left:605px;top:3113px;width:245px;height:216px;background:linear-gradient(160deg,#f0f0f0,#69c4cc 50%,#f09040)"></div>
  <div class="tile photo" role="img" aria-label="Green plush sea turtle" style="left:860px;top:2779px;width:246px;height:216px;background:linear-gradient(160deg,#dadada,#8fa98a 55%,#b7c44a)"></div>
  <div class="tile photo" role="img" aria-label="Beige plush puppy" style="left:860px;top:3005px;width:246px;height:324px;background:linear-gradient(160deg,#b9bcbe,#e2cd9c 55%,#d9c3a6)"></div>
</section>

<div class="steps-pill">Steps of Manufacturing</div>
<section class="steps">
  <svg class="abs" style="left:0;top:0" width="1200" height="542" viewBox="0 0 1200 542">
    <g fill="none" stroke="var(--brown)" stroke-width="2">
      <g transform="translate(243 275)"><path d="M-62 -62A88 88 0 0 0 -62 62M62 -62A88 88 0 0 1 62 62M-48 -48A68 68 0 0 0 -48 48M48 -48A68 68 0 0 1 48 48"/><path d="M0 -110V-56"/></g>
      <g transform="translate(481 275)"><path d="M-62 -62A88 88 0 0 0 -62 62M62 -62A88 88 0 0 1 62 62M-48 -48A68 68 0 0 0 -48 48M48 -48A68 68 0 0 1 48 48"/><path d="M0 56V110"/></g>
      <g transform="translate(721 275)"><path d="M-62 -62A88 88 0 0 0 -62 62M62 -62A88 88 0 0 1 62 62M-48 -48A68 68 0 0 0 -48 48M48 -48A68 68 0 0 1 48 48"/><path d="M0 -110V-56"/></g>
      <g transform="translate(958 275)"><path d="M-62 -62A88 88 0 0 0 -62 62M62 -62A88 88 0 0 1 62 62M-48 -48A68 68 0 0 0 -48 48M48 -48A68 68 0 0 1 48 48"/><path d="M0 56V110"/></g>
    </g>
    <g fill="var(--brown)">
      <circle cx="243" cy="165" r="4"/><circle cx="481" cy="385" r="4"/><circle cx="721" cy="165" r="4"/><circle cx="958" cy="385" r="4"/>
      <circle cx="243" cy="275" r="56"/><circle cx="481" cy="275" r="56"/><circle cx="721" cy="275" r="56"/><circle cx="958" cy="275" r="56"/>
    </g>
    <g fill="none" stroke="var(--gold)" stroke-width="3" stroke-linejoin="round">
      <path d="M243 252l14 18-14 22-14-22z M243 270v22"/>
      <rect x="701" y="255" width="40" height="40" rx="3" stroke-dasharray="5 3"/>
      <path d="M940 278l18-18 18 18-18 12z M944 296h30"/>
    </g>
    <g fill="var(--gold)"><circle cx="481" cy="262" r="10"/><circle cx="481" cy="288" r="14"/></g>
  </svg>
  <p class="mstep" style="left:351px;top:98px"><b>A Seamstress</b>Eaque ipsa quae ab illo inventore veritatis et quasi</p>
  <p class="mstep" style="left:828px;top:98px"><b>Selection of Color</b>Eaque ipsa quae ab illo inventore veritatis et quasi</p>
  <p class="mstep" style="left:113px;top:390px"><b>Designer at Work</b>Eaque ipsa quae ab illo inventore veritatis et quasi</p>
  <p class="mstep" style="left:591px;top:390px"><b>Selection of a Fabric</b>Eaque ipsa quae ab illo inventore veritatis et quasi</p>
</section>

<section aria-label="Contact">
  <h2 class="abs center section-title" style="top:4050px">Contact Us</h2>
  <p class="abs center eyebrow" style="top:4104px">Get in touch</p>
  <div class="field" style="left:243px;top:4180px;width:350px;height:53px">First Name</div>
  <div class="field" style="left:607px;top:4180px;width:350px;height:53px">Last Name</div>
  <div class="field" style="left:243px;top:4246px;width:350px;height:54px">Phone No</div>
  <div class="field" style="left:607px;top:4246px;width:350px;height:54px">Email Address</div>
  <div class="field" style="left:243px;top:4315px;width:714px;height:166px">Message</div>
  <a class="btn btn-outline" style="left:507px;top:4502px;width:184px;height:49px">Send Now <svg class="arrow" viewBox="0 0 26 10"><path d="M0 5h23M19 1l4 4-4 4" stroke="#fff" stroke-width="2" fill="none"/></svg></a>
</section>

<footer class="site-footer">
  <div class="abs" style="left:92px;top:88px;width:104px;height:104px;border-radius:50%;background:#fff;display:flex;align-items:center;justify-content:center"><span style="font-weight:700;font-size:15px;color:var(--brown)">PlushKeep</span></div>
  <div class="abs" style="left:92px;top:243px;display:flex;gap:20px">
    <span style="width:12px;height:12px;border-radius:50%;background:var(--orange)"></span>
    <span style="width:12px;height:12px;border-radius:50%;background:var(--orange)"></span>
    <span style="width:12px;height:12px;border-radius:50%;background:var(--orange)"></span>
    <span style="width:12px;height:12px;border-radius:50%;background:var(--orange)"></span>
  </div>
  <h3 class="foot-h" style="left:328px">Quick Links</h3>
  <a class="foot-l" style="left:328px;top:134px">Home</a>
  <a class="foot-l" style="left:328px;top:169px">Products</a>
  <a class="foot-l" style="left:328px;top:206px">Gallery</a>
  <a class="foot-l" style="left:328px;top:242px">Contact Us</a>
  <h3 class="foot-h" style="left:568px">Other Links</h3>
  <a class="foot-l" style="left:568px;top:134px">Privacy Policy</a>
  <a class="foot-l" style="left:568px;top:169px">Terms &amp; Condition</a>
  <a class="foot-l" style="left:568px;top:206px">Faq</a>
  <a class="foot-l" style="left:568px;top:242px">About Us</a>
  <h3 class="foot-h" style="left:847px">Contact Information</h3>
  <svg class="abs" style="left:847px;top:138px" width="14" height="18" viewBox="0 0 14 18"><path d="M7 0a7 7 0 0 0-7 7c0 5 7 11 7 11s7-6 7-11a7 7 0 0 0-7-7z" fill="var(--orange)"/><circle cx="7" cy="7" r="2.5" fill="var(--navy-deep)"/></svg>
  <p class="foot-l" style="left:880px;top:134px;width:240px;line-height:27px">totam rem aperiam eaque ipsa quae ab illo invent</p>
  <svg class="abs" style="left:847px;top:200px" width="16" height="16" viewBox="0 0 24 24" fill="var(--orange)"><path d="M6.6 10.8a15 15 0 0 0 6.6 6.6l2.2-2.2c.3-.3.7-.4 1-.2 1.1.4 2.3.6 3.6.6.6 0 1 .4 1 1V20c0 .6-.4 1-1 1A17 17 0 0 1 3 4c0-.6.4-1 1-1h3.5c.6 0 1 .4 1 1 0 1.3.2 2.5.6 3.6.1.3 0 .7-.2 1z"/></svg>
  <p class="foot-l" style="left:880px;top:197px">555-014-2290</p>
  <svg class="abs" style="left:847px;top:243px" width="16" height="12" viewBox="0 0 16 12"><rect width="16" height="12" rx="1" fill="var(--orange)"/><path d="M1 1l7 6 7-6" stroke="var(--navy-deep)" stroke-width="1.5" fill="none"/></svg>
  <p class="foot-l" style="left:880px;top:239px">hello@plushkeep.com</p>
  <div class="abs" style="left:92px;top:355px;width:1014px;height:1px;background:#3a3765"></div>
  <p class="abs center" style="top:383px;font-size:14px;color:#e7e6f2">Copyright © 2022 PlushKeep. All rights reserved.</p>
</footer>

</body>
</html>
```